Detox Before & After Charts

I am looking to create a chart/graph to be used to chart a patient's progress before and after using our 15-day detox program. We will be looking for 3 different graphs to be made.
1. A chart showing the before and after symptom scores of 12 patients in a small clinical trial we did. We will use this one to show prospective patients.
2. A chart showing one single patient's "total" symptom scores before and after the detox. We will use this with each patient, before and after they do the detox.
3. A chart showing one patient's before and symptom scores in more detail, showing their scores in each one of the symptom categories. We will do this with each patient, before and after the detox.
For #2 & #3 above, we would want a master template that we could add the scoring for each new patient ourselves.
See attached for rough samples.
Each of these 3 charts should be the same style, but for now, just do chart #3. And after we decide on the designer, then we will have them do the other 2 charts.
And I prefer a line graph over a bar graph for these. I did not mention that at first. Sorry!!

```html
<!DOCTYPE html>
<html lang="en">
<head>
<meta charset="utf-8">
<title>Detox Before &amp; After – Category Symptom Chart</title>
<link href="https://fonts.googleapis.com/css2?family=Carlito:wght@400;700&display=swap" rel="stylesheet">
<style>
:root{
  --page:#ffffff;
  --grid:#d9dde3;
  --grid-soft:#eceef1;
  --ink:#111111;
  --blue:#2e75b6;
  --blue-light:#9fc3e7;
  --axis-line:#bcd6ee;
  --red:#c00000;
  --red-bright:#ff0000;
  --green:#548235;
  --green-light:#a9d18e;
  --card-line:#c8c8c8;
}
*{margin:0;padding:0;box-sizing:border-box}
html,body{width:1200px;height:923px;overflow:hidden;background:var(--page)}
body{font-family:"Carlito","Calibri",sans-serif;color:var(--ink)}
.sheet{position:absolute;left:0;top:33px;width:1080px;height:772px;transform:scale(1.1111);transform-origin:0 0;
  background:
   repeating-linear-gradient(to bottom,transparent 0 12.5px,var(--grid-soft) 12.5px 13.5px),
   repeating-linear-gradient(to right,transparent 0 50px,var(--grid-soft) 50px 51px);
}
.data-table{position:absolute;left:0;top:0;border-collapse:collapse;font-size:10px;background:#fff}
.data-table td{height:13.6px;width:51px;border:1px solid var(--grid);padding:0 2px;white-space:nowrap;overflow:hidden;line-height:12px}
.data-table td.row-label{width:66px;text-align:left}
.data-table td.num{text-align:right}
.card{position:absolute;left:11px;top:60px;width:1057px;height:699px;background:#fff;border:1px solid #e0e0e0;border-radius:10px}
.field-label{position:absolute;font-weight:700;font-size:13px;color:var(--blue)}
.field-box,.panel,.panel-head,.value-box{position:absolute;background:#fff;border:1px solid var(--card-line);box-shadow:2px 2px 3px rgba(0,0,0,.25)}
.field-box{border-radius:8px}
.panel{border-radius:16px}
.panel-head{border-radius:8px;display:flex;align-items:center;justify-content:center;font-size:25px}
.panel-head.before{color:var(--red)}
.panel-head.after{color:var(--green)}
.panel-head.change{color:var(--blue)}
.panel-label{position:absolute;font-weight:700;font-size:11.5px;line-height:16px}
.value-box{border-radius:4px;font-weight:700;font-size:12px;display:flex;align-items:center;justify-content:flex-end;padding-right:9px;box-shadow:1px 1px 2px rgba(0,0,0,.25)}
.value-box.before{color:var(--red)}
.value-box.after{color:var(--green)}
.value-box.change{color:var(--blue)}
.axis-title{position:absolute;left:20px;top:266px;width:40px;height:339px;border-radius:5px;background:linear-gradient(to right,#5b9bd5,#9fc3e7);display:flex;align-items:center;justify-content:center}
.axis-title span{transform:rotate(-90deg);white-space:nowrap;color:#fff;font-size:22px}
.legend-bar{position:absolute;left:1015px;width:33px;border-radius:4px;display:flex;align-items:center;justify-content:center}
.legend-bar span{transform:rotate(90deg);white-space:nowrap;color:#fff;font-size:22px}
.legend-bar.before{top:246px;height:331px;background:linear-gradient(to bottom,#c00000,#ff0000)}
.legend-bar.after{top:581px;height:113px;background:linear-gradient(to bottom,#548235,#a9d18e)}
.chart{position:absolute;left:0;top:0;width:1080px;height:772px;overflow:visible}
.chart text{font-family:"Carlito","Calibri",sans-serif}
.tick{fill:var(--blue);font-weight:700;font-size:13px}
.cat{fill:var(--blue);font-weight:700;font-size:11px}
.bubble-before ellipse{fill:#fff;stroke:var(--red);stroke-width:1.2}
.bubble-before text{fill:var(--red);font-weight:700;font-size:9.5px}
.bubble-after ellipse{fill:#fff;stroke:var(--green-light);stroke-width:1.2}
.bubble-after text{fill:#375623;font-weight:700;font-size:9.5px}
</style>
</head>
<body>
<div class="sheet">
  <table class="data-table">
    <tr><td class="row-label"></td><td>DIGESTION</td><td>EARS</td><td>EYES</td><td>LUNGS</td><td>MIND</td><td>ENERGY</td><td>HEAD</td><td>EMOTIONS</td><td>MOUTH</td><td>SKIN</td><td>PAIN</td><td>NOSE</td><td>HEART</td><td>WEIGHT</td></tr>
    <tr><td class="row-label">BEFORE</td><td class="num">12%</td><td class="num">12%</td><td class="num">25%</td><td class="num">12%</td><td class="num">12%</td><td class="num">12%</td><td class="num">37%</td><td class="num">31%</td><td class="num">20%</td><td class="num">45%</td><td class="num">100%</td><td class="num">30%</td><td class="num">25%</td><td class="num">40%</td></tr>
    <tr><td class="row-label">AFTER</td><td class="num">12%</td><td class="num">0%</td><td class="num">0%</td><td class="num">0%</td><td class="num">0%</td><td class="num">6%</td><td class="num">0%</td><td class="num">0%</td><td class="num">5%</td><td class="num">10%</td><td class="num">15%</td><td class="num">5%</td><td class="num">0%</td><td class="num">0%</td></tr>
  </table>

  <div class="card"></div>

  <div class="field-label" style="left:28px;top:110px">First Name</div>
  <div class="field-box" style="left:104px;top:97px;width:213px;height:43px"></div>
  <div class="field-label" style="left:28px;top:159px">Last Name</div>
  <div class="field-box" style="left:104px;top:148px;width:213px;height:42px"></div>

  <div class="panel" style="left:340px;top:92px;width:209px;height:128px"></div>
  <div class="panel-head before" style="left:351px;top:68px;width:185px;height:45px">BEFORE</div>
  <div class="panel-label" style="left:371px;top:124px">DATE:</div>
  <div class="panel-label" style="left:369px;top:146px">Total<br>Symptom<br>Scores:</div>
  <div class="panel-label" style="left:369px;top:196px">Weight:</div>
  <div class="value-box before" style="left:438px;top:120px;width:75px;height:25px">6/1/2012</div>
  <div class="value-box before" style="left:438px;top:156px;width:75px;height:25px">75</div>
  <div class="value-box before" style="left:438px;top:190px;width:75px;height:25px">140</div>

  <div class="panel" style="left:590px;top:92px;width:209px;height:128px"></div>
  <div class="panel-head after" style="left:601px;top:67px;width:185px;height:45px">AFTER</div>
  <div class="panel-label" style="left:621px;top:124px">DATE:</div>
  <div class="panel-label" style="left:619px;top:144px">Total<br>Symptom<br>Scores:</div>
  <div class="panel-label" style="left:618px;top:194px">Weight:</div>
  <div class="value-box after" style="left:689px;top:121px;width:75px;height:25px">6/16/2018</div>
  <div class="value-box after" style="left:689px;top:155px;width:75px;height:25px">75</div>
  <div class="value-box after" style="left:689px;top:189px;width:75px;height:25px">140</div>

  <div class="panel" style="left:834px;top:93px;width:185px;height:128px"></div>
  <div class="panel-head change" style="left:845px;top:69px;width:160px;height:45px">CHANGE</div>
  <div class="panel-label" style="left:862px;top:130px">Total<br>Symptom<br>Scores:</div>
  <div class="panel-label" style="left:862px;top:190px">Weight:</div>
  <div class="value-box change" style="left:922px;top:141px;width:68px;height:26px">-66%</div>
  <div class="value-box change" style="left:922px;top:184px;width:68px;height:25px">-9</div>

  <div class="axis-title"><span>CATEGORIE SYMPTOM SCORE</span></div>
  <div class="legend-bar before"><span>BEFORE</span></div>
  <div class="legend-bar after"><span>AFTER</span></div>

  <svg class="chart" viewBox="0 0 1080 772" role="img" aria-label="Line chart of category symptom scores before and after the detox">
    <g stroke="var(--axis-line)" stroke-width="1">
      <line x1="108" y1="244" x2="977" y2="244"/>
      <line x1="170" y1="244" x2="170" y2="691"/><line x1="232" y1="244" x2="232" y2="691"/>
      <line x1="294" y1="244" x2="294" y2="691"/><line x1="356" y1="244" x2="356" y2="691"/>
      <line x1="418" y1="244" x2="418" y2="691"/><line x1="480" y1="244" x2="480" y2="691"/>
      <line x1="542" y1="244" x2="542" y2="691"/><line x1="604" y1="244" x2="604" y2="691"/>
      <line x1="666" y1="244" x2="666" y2="691"/><line x1="728" y1="244" x2="728" y2="691"/>
      <line x1="790" y1="244" x2="790" y2="691"/><line x1="852" y1="244" x2="852" y2="691"/>
      <line x1="914" y1="244" x2="914" y2="691"/>
    </g>
    <line x1="108" y1="244" x2="108" y2="691" stroke="var(--blue)" stroke-width="1"/>
    <line x1="977" y1="244" x2="977" y2="691" stroke="var(--blue)" stroke-width="1"/>
    <line x1="108" y1="578" x2="977" y2="578" stroke="var(--blue)" stroke-width="1.3" stroke-dasharray="2 2"/>

    <g class="tick" text-anchor="end">
      <text x="94" y="249">100%</text><text x="94" y="325">80%</text><text x="94" y="401">60%</text>
      <text x="94" y="476">40%</text><text x="94" y="552">20%</text><text x="94" y="628">0%</text>
    </g>
    <g class="cat" text-anchor="middle">
      <text x="170" y="718">DIGESTION</text><text x="232" y="718">EARS</text><text x="294" y="718">EYES</text>
      <text x="356" y="718">LUNGS</text><text x="418" y="718">MIND</text><text x="480" y="718">ENERGY</text>
      <text x="542" y="718">HEAD</text><text x="604" y="718">EMOTIONS</text><text x="666" y="718">MOUTH</text>
      <text x="728" y="718">SKIN</text><text x="790" y="718">PAIN</text><text x="852" y="718">NOSE</text>
      <text x="914" y="718">HEART</text><text x="976" y="718">WEIGHT</text>
    </g>

    <path fill="none" stroke="var(--green)" stroke-width="2.5" d="M170 578 C195 578 207 623 232 623 C257 623 269 623 294 623 C319 623 331 623 356 623 C381 623 393 623 418 623 C443 623 455 600 480 600 C505 600 517 623 542 623 C567 623 579 623 604 623 C629 623 641 604 666 604 C691 604 703 585 728 585 C753 585 765 566 790 566 C815 566 827 604 852 604 C877 604 889 623 914 623 C939 623 951 623 976 623"/>
    <path fill="none" stroke="var(--red)" stroke-width="2.5" d="M170 578 C195 578 207 578 232 578 C257 578 269 528 294 528 C319 528 331 578 356 578 C381 578 393 578 418 578 C443 578 455 578 480 578 C505 578 517 483 542 483 C567 483 579 505 604 505 C629 505 641 547 666 547 C691 547 703 500 728 452 C760 390 770 244 790 244 C815 244 827 509 852 509 C877 509 889 528 914 528 C939 528 951 490 976 471"/>

    <g stroke="var(--green-light)" stroke-width="1">
      <line x1="170" y1="578" x2="155" y2="603"/><line x1="232" y1="623" x2="240" y2="599"/><line x1="294" y1="623" x2="291" y2="595"/>
      <line x1="356" y1="623" x2="353" y2="599"/><line x1="418" y1="623" x2="409" y2="601"/><line x1="480" y1="600" x2="506" y2="587"/>
      <line x1="542" y1="623" x2="545" y2="598"/><line x1="604" y1="623" x2="596" y2="595"/><line x1="666" y1="604" x2="667" y2="580"/>
      <line x1="728" y1="585" x2="728" y2="561"/><line x1="790" y1="566" x2="792" y2="544"/><line x1="852" y1="604" x2="860" y2="578"/>
      <line x1="914" y1="623" x2="919" y2="596"/><line x1="976" y1="623" x2="981" y2="596"/>
    </g>
    <g stroke="var(--red)" stroke-width="1">
      <line x1="170" y1="578" x2="207" y2="566"/><line x1="232" y1="578" x2="240" y2="544"/><line x1="294" y1="528" x2="318" y2="509"/>
      <line x1="356" y1="578" x2="370" y2="546"/><line x1="418" y1="578" x2="425" y2="539"/><line x1="480" y1="578" x2="476" y2="536"/>
      <line x1="542" y1="483" x2="534" y2="448"/><line x1="604" y1="505" x2="613" y2="469"/><line x1="666" y1="547" x2="647" y2="518"/>
      <line x1="728" y1="452" x2="693" y2="429"/><line x1="790" y1="244" x2="832" y2="247"/><line x1="852" y1="509" x2="869" y2="466"/>
      <line x1="914" y1="528" x2="918" y2="485"/><line x1="976" y1="471" x2="971" y2="440"/>
    </g>

    <g class="bubble-after" text-anchor="middle">
      <g transform="translate(155 603)"><ellipse rx="17" ry="10"/><text y="3.5">12%</text></g>
      <g transform="translate(240 599)"><ellipse rx="15" ry="10"/><text y="3.5">0%</text></g>
      <g transform="translate(291 595)"><ellipse rx="15" ry="10"/><text y="3.5">0%</text></g>
      <g transform="translate(353 599)"><ellipse rx="15" ry="10"/><text y="3.5">0%</text></g>
      <g transform="translate(409 601)"><ellipse rx="15" ry="10"/><text y="3.5">0%</text></g>
      <g transform="translate(506 587)"><ellipse rx="15" ry="10"/><text y="3.5">6%</text></g>
      <g transform="translate(545 598)"><ellipse rx="15" ry="10"/><text y="3.5">0%</text></g>
      <g transform="translate(596 595)"><ellipse rx="15" ry="10"/><text y="3.5">0%</text></g>
      <g transform="translate(667 580)"><ellipse rx="15" ry="10"/><text y="3.5">5%</text></g>
      <g transform="translate(728 561)"><ellipse rx="17" ry="10"/><text y="3.5">10%</text></g>
      <g transform="translate(792 544)"><ellipse rx="17" ry="10"/><text y="3.5">15%</text></g>
      <g transform="translate(860 578)"><ellipse rx="15" ry="10"/><text y="3.5">5%</text></g>
      <g transform="translate(919 596)"><ellipse rx="15" ry="10"/><text y="3.5">0%</text></g>
      <g transform="translate(981 596)"><ellipse rx="15" ry="10"/><text y="3.5">0%</text></g>
    </g>
    <g class="bubble-before" text-anchor="middle">
      <g transform="translate(207 566)"><ellipse rx="17" ry="10"/><text y="3.5">12%</text></g>
      <g transform="translate(240 544)"><ellipse rx="17" ry="10"/><text y="3.5">12%</text></g>
      <g transform="translate(318 509)"><ellipse rx="17" ry="10"/><text y="3.5">25%</text></g>
      <g transform="translate(370 546)"><ellipse rx="17" ry="10"/><text y="3.5">12%</text></g>
      <g transform="translate(425 539)"><ellipse rx="17" ry="10"/><text y="3.5">12%</text></g>
      <g transform="translate(476 536)"><ellipse rx="17" ry="10"/><text y="3.5">12%</text></g>
      <g transform="translate(534 448)"><ellipse rx="17" ry="10"/><text y="3.5">37%</text></g>
      <g transform="translate(613 469)"><ellipse rx="17" ry="10"/><text y="3.5">31%</text></g>
      <g transform="translate(647 518)"><ellipse rx="17" ry="10"/><text y="3.5">20%</text></g>
      <g transform="translate(693 429)"><ellipse rx="17" ry="10"/><text y="3.5">45%</text></g>
      <g transform="translate(832 247)"><ellipse rx="21" ry="10"/><text y="3.5">100%</text></g>
      <g transform="translate(869 466)"><ellipse rx="17" ry="10"/><text y="3.5">30%</text></g>
      <g transform="translate(918 485)"><ellipse rx="17" ry="10"/><text y="3.5">25%</text></g>
      <g transform="translate(971 440)"><ellipse rx="17" ry="10"/><text y="3.5">40%</text></g>
    </g>
  </svg>
</div>
</body>
</html>
```